QELV MAX PowerPoint

I need to convert our online business to a power point. A step by step presentation,
I want a POWER POINT to use one on one and as well as for a group.
Like to see moving parts to show value and savings. Very clear " dream Vacation" pictures. This is the future of vacationing!

web site:
QELV.online

two videos below to be included
Updates

The first four days i never received anything. Their was a mixup regarding my power point.

Target Market(s)

dream vacations, for everyone

Number of Pages Required

5+ page

Font styles to use
Sans Serif

Colors

Designer to choose colors to be used in the design.

Requirements
Must have
• Look professional
• movement
Nice to have
• Easy to understand and use. show savings and value
• 10 to 20 pages min.
Should not have
• look nothing like my old power point

```html
<!DOCTYPE html>
<html lang="en">
<head>
<meta charset="utf-8">
<title>QELV MAX Presentation Deck</title>
<link href="https://fonts.googleapis.com/css2?family=Lato:wght@300;400;700;900&display=swap" rel="stylesheet">
<style>
:root{
  --blue:#14a2e6;
  --green:#79c143;
  --yellow:#f6c419;
  --ink:#333333;
  --muted:#8c8c8c;
  --navy:#1d3a86;
  --canvas:#ececec;
  --panel:#e6e6e6;
}
*{box-sizing:border-box;margin:0;padding:0}
html,body{width:1200px;height:1200px;overflow:hidden}
body{background:var(--canvas);font-family:'Lato',sans-serif;color:var(--ink);position:relative}
.sprite{position:absolute;width:0;height:0}

.slide{position:absolute;width:290px;height:162px;background:#fff;overflow:hidden;box-shadow:0 2px 4px rgba(0,0,0,.35)}
.slide>*{position:absolute}
.c1{left:11px}.c2{left:308px}.c3{left:605px}.c4{left:902px}
.r1{top:8px}.r2{top:178px}.r3{top:349px}.r4{top:519px}.r5{top:690px}.r6{top:860px}.r7{top:1030px}
.slide.grey{background:var(--panel)}

.title{font-weight:300;font-size:10px;line-height:1.15;color:var(--ink)}
.title b{font-weight:700}
.center{text-align:center}
.tx{font-size:3.6px;line-height:1.45;color:var(--muted)}
.lbl{font-size:4.2px;font-weight:700;color:var(--ink);text-transform:uppercase;letter-spacing:.1px}
.cap{font-size:3.4px;color:var(--muted);text-transform:uppercase;letter-spacing:.2px}
.brand{font-size:6px;font-weight:700;color:var(--navy);letter-spacing:.2px}
.white{color:#fff}
.blue{color:var(--blue)}.green{color:var(--green)}.yellow{color:var(--yellow)}
.bg-blue{background:var(--blue)}.bg-green{background:var(--green)}.bg-yellow{background:var(--yellow)}
.ic{width:10px;height:10px;fill:currentColor;display:block}
.btn{font-size:3.8px;font-weight:700;color:#fff;display:flex;align-items:center;justify-content:center;text-transform:uppercase}

/* image areas */
.ph{display:block}
.p-beach{background:linear-gradient(180deg,#9fd2ee 0%,#74b8dc 42%,#d8c7a5 66%,#8d7a62 100%)}
.p-sea{background:linear-gradient(180deg,#8fd0f0 0%,#5bb7e0 50%,#2f9fc9 100%)}
.p-land{background:linear-gradient(180deg,#cfe4f3 0%,#e9efe0 40%,#9fbf5a 62%,#6e8f36 100%)}
.p-pool{background:linear-gradient(180deg,#9fd6f3 0%,#d9a15a 45%,#3fb6b0 72%,#1e8e8a 100%)}
.p-hut{background:linear-gradient(180deg,#6fb8d8 0%,#a9d8e8 40%,#7a5a3c 58%,#2fa9b5 80%,#177f8c 100%)}
.p-room{background:linear-gradient(135deg,#c69a6c 0%,#e8d3b6 45%,#f4efe8 70%,#a88260 100%)}
.p-jungle{background:linear-gradient(180deg,#1f4a22 0%,#3f7a2e 45%,#87a860 80%,#c9d4b0 100%)}
.p-bw{background:linear-gradient(135deg,#3a3a3a 0%,#9a9a9a 50%,#d4d4d4 100%)}
.p-people{background:linear-gradient(135deg,#c7a07a 0%,#e7cfb2 40%,#7a8fa8 75%,#3f5a78 100%)}
.p-city{background:linear-gradient(180deg,#b9d8ef 0%,#e8e4da 50%,#c7b79c 100%)}
.p-sun{background:linear-gradient(180deg,#f2c46a 0%,#f3a55a 40%,#5ab7d6 70%,#2f90b5 100%)}

/* slide 3 */
.sky{background:linear-gradient(180deg,#d7ecfa 0%,#b7dcf4 100%)}
.orbit-title{font-size:17px;font-weight:900;color:#1b2f6b;letter-spacing:.3px;width:290px;text-align:center}
.orbit-sub{font-size:7.5px;font-weight:700;color:#2f61b3;width:290px;text-align:center;letter-spacing:.4px}
.split-band{width:145px;height:38px;text-align:center;padding-top:5px}
.split-band .big{font-size:11px;color:#fff;font-weight:400}
.split-band .big sup{font-size:5px}
.split-band .big span{color:var(--yellow);font-size:8px}
.split-band .tx{color:#fff;padding:0 14px}

/* generic lists */
.dot-list{list-style:none;font-size:3.6px;line-height:1.55;color:#666}
.dot-list li::before{content:"▸ ";color:var(--green)}
.white-list{list-style:none;font-size:3.6px;line-height:1.5;color:#fff}
.white-list li::before{content:"• "}

/* feature grids */
.feat{display:grid;text-align:center;justify-items:center;row-gap:8px}
.feat .ic{margin-bottom:4px}
.feat .tx{width:70px}

/* price cards */
.rate-card{width:78px;height:100px;border:1px solid #e2e2e2;background:#fff;text-align:center;padding-top:7px}
.rate-card .ic{margin:0 auto;color:#555}
.rate-card .name{font-size:6.5px;font-weight:300;color:#555;margin:4px 0}
.rate-card .price{height:12px;font-size:4.5px;font-weight:700;color:#fff;line-height:12px}
.rate-card ul{list-style:none;text-align:left;padding:7px 0 0 8px;font-size:3.4px;line-height:1.6;color:#999}
.rate-card li::before{content:"– "}

.trip-card{width:62px;height:62px;background:#fff;text-align:center;padding-top:6px;box-shadow:0 1px 2px rgba(0,0,0,.2)}
.trip-card .ic{margin:0 auto;color:var(--blue);width:12px;height:12px}
.trip-card .days{font-size:5px;color:#888;margin:4px 0 3px}
.trip-card .bar{height:10px;font-size:3.8px;font-weight:700;color:#fff;line-height:10px}
.trip-card .tx{margin-top:4px}

.tile-label{font-size:13px;font-weight:300;color:#fff;text-align:center;width:134px;line-height:1}
.tile-label small{display:block;font-size:3.5px;letter-spacing:.3px}

.own-card{width:62px;height:84px;border:1px solid #ddd;background:#fff;text-align:center;padding-top:6px}
.own-card .lbl{color:var(--blue)}
.own-card .round{width:36px;height:36px;border-radius:50%;margin:6px auto}
.own-card .box{font-size:3.6px;border:1px solid #bbb;width:42px;margin:10px auto 0;padding:1px}
.own-list{list-style:none;font-size:3.2px;line-height:1.6;color:#555;font-weight:700;text-transform:uppercase}
.own-list li::before{content:"• ";color:var(--blue)}

.dest-card{width:112px;height:112px;background:#fff;border:1px solid #ddd;box-shadow:0 1px 3px rgba(0,0,0,.25);padding:12px 14px}
.dest-card .name{font-size:11px;font-weight:400}
.dest-card .bar{height:10px;background:var(--yellow);color:#fff;font-size:3.4px;font-weight:700;line-height:10px;text-align:center;margin:6px 0 7px}
.dest-card .icons{display:flex;gap:12px;margin-bottom:6px}
.dest-card .icons .ic{width:8px;height:8px}

.pack{background:#fff;box-shadow:0 1px 3px rgba(0,0,0,.25);text-align:center}
.pack .img{height:44px}
.pack .kind{font-size:3px;color:var(--blue);font-weight:700;margin-top:4px}
.pack .name{font-size:6px;margin:2px 0}
.pack .meta{display:flex;justify-content:space-around;font-size:3.2px;color:#777;margin-top:4px}
.pack .meta span b{display:block;color:var(--yellow);font-weight:400}

.event{background:#fff;text-align:center}
.event .img{height:56px}
.event .free{width:46px;height:6px;margin:-3px auto 0;background:var(--yellow);color:#fff;font-size:3px;font-weight:700;line-height:6px;position:relative}
.event .date{font-size:3.2px;font-weight:700;margin-top:5px}
.event .name{font-size:7px;margin:4px 0 3px}
.event .tx{padding:0 8px}

.offer{width:124px;height:58px;background:#fff;display:flex}
.offer .img{width:58px;height:58px}
.offer .info{padding:5px 5px}
.offer .price{font-size:7px;color:var(--blue);font-weight:700}
.offer .price small{font-size:2.8px;color:#777;font-weight:400;vertical-align:middle}
.offer .dots{display:flex;gap:4px;margin-top:4px}
.offer .dots i{width:4px;height:3px;background:var(--yellow);display:block}

.side{background:var(--blue);width:68px;height:162px;display:flex;flex-direction:column;align-items:center;justify-content:space-around;padding:8px 0;color:#fff}
.side div{text-align:center;font-size:3.2px;font-weight:700;text-transform:uppercase;line-height:1.3}
.side .ic{margin:0 auto 2px;width:11px;height:11px}

.strip{display:flex}
.strip span{flex:1;display:block}

.partner{width:42px;height:28px;background:#f4f4f4;display:flex;align-items:center;justify-content:center}
.partner i{display:block;width:24px;height:6px;border-radius:3px}
</style>
</head>
<body>

<svg class="sprite" aria-hidden="true">
  <symbol id="i-plane" viewBox="0 0 24 24"><path d="M21 16v-2l-8-5V3.5a1.5 1.5 0 0 0-3 0V9l-8 5v2l8-2.5V19l-2 1.5V22l3.5-1 3.5 1v-1.5L13 19v-5.5z"/></symbol>
  <symbol id="i-sail" viewBox="0 0 24 24"><path d="M11 2v16H3zM13 5l7 13h-7zM2 20h20l-2 2H4z"/></symbol>
  <symbol id="i-hotel" viewBox="0 0 24 24"><path fill-rule="evenodd" d="M3 4h18v17H3zM6 7v3h3V7zm5 0v3h3V7zm5 0v3h3V7zM6 12v3h3v-3zm10 0v3h3v-3zM10 14v7h4v-7z"/></symbol>
  <symbol id="i-globe" viewBox="0 0 24 24"><g fill="none" stroke="currentColor" stroke-width="2"><circle cx="12" cy="12" r="9"/><ellipse cx="12" cy="12" rx="4" ry="9"/><path d="M3 12h18"/></g></symbol>
  <symbol id="i-people" viewBox="0 0 24 24"><circle cx="8" cy="5" r="2.5"/><circle cx="16" cy="5" r="2.5"/><path d="M5 9h6l1 7h-2v6H6v-6H4zm8 0h6l1 7h-2v6h-4v-6h-2z"/></symbol>
  <symbol id="i-car" viewBox="0 0 24 24"><path d="M5 11l2-5h10l2 5h1v6h-2v2h-3v-2H9v2H6v-2H4v-6z"/></symbol>
  <symbol id="i-star" viewBox="0 0 24 24"><path d="M12 2l3 7h7l-5.5 4.5 2 7.5L12 17l-6.5 4 2-7.5L2 9h7z"/></symbol>
  <symbol id="i-bed" viewBox="0 0 24 24"><path d="M2 6h3v7h17v7h-3v-3H5v3H2zM7 9h5v3H7zM13 9h7v3h-7z"/></symbol>
  <symbol id="i-tag" viewBox="0 0 24 24"><path d="M3 3h9l9 9-9 9-9-9zM7 6a1.5 1.5 0 1 0 0 3 1.5 1.5 0 0 0 0-3z"/></symbol>
  <symbol id="i-sun" viewBox="0 0 24 24"><circle cx="12" cy="12" r="6"/></symbol>
</svg>

<!-- Row 1 -->
<section class="slide c1 r1">
  <div class="ph p-beach" role="img" aria-label="Couple relaxing on a seaside wall above a sunny beach" style="inset:0"></div>
  <div class="brand" style="left:8px;top:8px">QELV</div>
  <div class="white" style="left:24px;top:74px;font-size:24px;font-weight:400">It's Never</div>
  <div class="yellow" style="left:24px;top:104px;font-size:11px">Too Late</div>
</section>

<section class="slide c2 r1">
  <div class="cap" style="left:19px;top:14px">Package based on adventure type</div>
  <div class="title" style="left:19px;top:23px"><span class="yellow">Welcome to</span> QELV MAX</div>
  <div class="feat" style="left:10px;top:50px;width:270px;grid-template-columns:repeat(3,1fr);row-gap:10px">
    <div class="lbl"><svg class="ic blue" style="margin:0 auto 4px"><use href="#i-hotel"/></svg>Hotels</div>
    <div class="lbl"><svg class="ic green" style="margin:0 auto 4px"><use href="#i-sail"/></svg>Cruises</div>
    <div class="lbl"><svg class="ic yellow" style="margin:0 auto 4px"><use href="#i-bed"/></svg>Weekly Stays</div>
    <div class="lbl"><svg class="ic green" style="margin:0 auto 4px"><use href="#i-people"/></svg>Activities</div>
    <div class="lbl"><svg class="ic yellow" style="margin:0 auto 4px"><use href="#i-sail"/></svg>Yachts</div>
    <div class="lbl"><svg class="ic blue" style="margin:0 auto 4px"><use href="#i-globe"/></svg>World Tours</div>
  </div>
  <div class="strip" role="img" aria-label="Row of travel photos: beach, hotel room, pool and resort" style="left:0;top:124px;width:290px;height:38px">
    <span class="p-sea"></span><span class="p-room"></span><span class="p-land"></span><span class="p-city"></span><span class="p-pool"></span>
  </div>
</section>

<section class="slide c3 r1 sky">
  <div class="ph" role="img" aria-label="Soft white clouds in a pale blue sky" style="inset:0 0 38px 0;background:radial-gradient(ellipse 40px 16px at 70px 30px,#fff 90%,transparent),radial-gradient(ellipse 50px 18px at 220px 42px,#fff 90%,transparent),radial-gradient(ellipse 30px 10px at 150px 110px,#fff 90%,transparent)"></div>
  <div class="orbit-title" style="left:0;top:70px">ORBIT REWARDS</div>
  <div class="orbit-sub" style="left:0;top:94px">Send Savings. Receive Rewards.</div>
  <div class="split-band bg-blue" style="left:0;top:124px">
    <div class="big">50<sup>%</sup> <span>FOR YOU</span></div>
    <div class="tx">Earn 50% of the savings in Reward Credits when friends book hotels.</div>
  </div>
  <div class="split-band bg-green" style="left:145px;top:124px">
    <div class="big">50<sup>%</sup> <span>FOR FRIENDS</span></div>
    <div class="tx">Friends receive 50% of your savings on top hotels and resorts worldwide</div>
  </div>
</section>

<section class="slide c4 r1">
  <div class="ph p-land" role="img" aria-label="Hiker with backpack overlooking green hills" style="inset:0"></div>
  <div class="brand" style="right:8px;top:8px">QELV</div>
  <div style="left:18px;top:11px;font-size:8px;line-height:1.2">QELV MAX<br>Offers a <span class="blue">Best Rate Guarantee</span><br>at Time of Booking</div>
  <div class="tx" style="left:18px;top:50px;width:125px;color:#444">We promise to credit you 110% of the price difference if you find cheaper pricing online after you make a reservation through your membership. Simply submit a claim within 24 hours from booking.</div>
  <div class="btn bg-blue" style="left:18px;top:92px;width:105px;height:13px">▶&nbsp; Best Rate Guarantee</div>
</section>

<!-- Row 2 -->
<section class="slide c1 r2">
  <div class="ph p-people" role="img" aria-label="Smiling couple taking a selfie in the city" style="left:0;top:0;width:144px;height:112px"></div>
  <div class="bg-yellow white" style="left:0;top:78px;width:118px;height:18px;font-size:10px;padding:3px 0 0 16px">Reward Credits</div>
  <div class="bg-blue" style="left:0;top:112px;width:144px;height:50px"></div>
  <div class="tx white center" style="left:14px;top:124px;width:116px">As a Member with QELV MAX you Earn Reward Credits on Everything you purchase through your Membership even when your not on Vacation.</div>
  <div class="title" style="left:158px;top:12px">Earn Reward<br>Credit on:</div>
  <ul class="dot-list" style="left:158px;top:48px"><li>All Accommodations</li><li>Flight</li><li>Cruises</li><li>Vacation Packages</li><li>Car Rentals</li></ul>
  <ul class="dot-list" style="left:222px;top:48px"><li>Concert &amp; Theatre Tickets</li><li>Sporting Events</li><li>Activities</li><li>Dining</li><li>Thousands of Online Shops</li></ul>
  <div class="tx" style="left:158px;top:102px;width:120px;color:#666">Reward Credits are just like Cash. Use them right away or save them for that Special Dream Vacation you've always wanted. With all the Discount and Savings along with Reward Credits, your Membership gives you and your Family a Lifetime of Incredible Value and Unforgettable Memories.</div>
</section>

<section class="slide c2 r2">
  <div class="ph p-bw" role="img" aria-label="Man in black and white looking thoughtful" style="left:0;top:0;width:145px;height:112px"></div>
  <div class="ph p-land" role="img" aria-label="Couple jumping joyfully in an open field" style="left:145px;top:0;width:145px;height:112px"></div>
  <div style="left:0;top:88px;width:118px;height:12px;background:rgba(246,196,25,.55);font-size:8px;color:#fff;padding-left:22px">Your Way - <b style="color:var(--yellow)">Rent</b></div>
  <div class="bg-blue" style="left:172px;top:88px;width:118px;height:12px;font-size:8px;color:#fff;padding-left:24px">NextGen - <b style="color:#1c2b55">Own</b></div>
  <div class="bg-yellow" style="left:0;top:112px;width:145px;height:50px"></div>
  <div class="bg-green" style="left:145px;top:112px;width:145px;height:50px"></div>
  <ul class="white-list" style="left:20px;top:116px"><li>Airfare</li><li>Hotels</li><li>Activities</li><li>Car Rental</li><li>Food</li></ul>
  <div class="white-list" style="left:76px;top:116px">MEMORIES<br>Total = $3000<br>No money put BACK<br>into the account, NO<br>VACATIONS!</div>
  <ul class="white-list" style="left:165px;top:116px"><li>Airfare</li><li>Hotels</li><li>Activities</li><li>Car Rental</li><li>Food</li></ul>
  <div class="white-list" style="left:215px;top:116px">MEMORIES<br>Total = $1162<br>Reward credits - 76,340<br>Next vacation PAID!</div>
</section>

<section class="slide c3 r2">
  <div class="title" style="left:20px;top:14px;width:100px;text-align:right">Total Hotel Room<br>Breakdown</div>
  <div style="left:40px;top:48px;width:80px;text-align:right">
    <div class="lbl" style="text-transform:none;font-weight:400;font-size:3.8px">True Net Price</div>
    <div class="tx">Book your flight, hotel, excursions and more all in one place.</div>
    <div style="font-size:3.8px;color:var(--blue);margin-top:5px">Consumer Price</div>
    <div class="tx">Book your flight, hotel, excursions and more all in one place.</div>
    <div style="font-size:3.8px;color:var(--yellow);margin-top:5px">Travel Agent</div>
    <div class="tx">Book your flight, hotel, excursions and more all in one place.</div>
    <div style="font-size:3.8px;color:var(--yellow);margin-top:5px">Wholesale Price</div>
    <div class="tx">Book your flight, hotel, excursions and more all in one place.</div>
  </div>
  <svg style="left:140px;top:14px" width="124" height="124" viewBox="-62 -62 124 124" aria-label="Pie chart of room price breakdown">
    <circle r="58" fill="none" stroke="#e4e4e4" stroke-width=".6"/>
    <path d="M0 0L0 -45A45 45 0 0 1 26.45 -36.41Z" fill="#f6c419"/>
    <path d="M0 0L26.45 -36.41A45 45 0 1 1 -36.41 26.45Z" fill="#4a4a4a"/>
    <path d="M0 0L-36.41 26.45A45 45 0 0 1 -26.45 -36.41Z" fill="#14a2e6"/>
    <path d="M0 0L-26.45 -36.41A45 45 0 0 1 0 -45Z" fill="#79c143"/>
    <g font-family="Lato,sans-serif" font-size="5" fill="#fff" opacity=".85">
      <text x="20" y="8">55%</text><text x="-30" y="12">25%</text><text x="-20" y="-20">10%</text><text x="6" y="-32">10%</text>
    </g>
    <circle cx="0" cy="-58" r="2.5" fill="#79c143"/><circle cx="41" cy="41" r="2.5" fill="#f6c419"/>
  </svg>
  <svg class="ic yellow" style="left:148px;top:64px;width:12px;height:12px"><use href="#i-plane"/></svg>
  <svg class="ic blue" style="left:246px;top:34px"><use href="#i-globe"/></svg>
  <div class="brand" style="left:4px;bottom:4px">QELV</div>
</section>

<section class="slide c4 r2">
  <div class="side">
    <div><svg class="ic"><use href="#i-hotel"/></svg>Hotels</div>
    <div><svg class="ic"><use href="#i-sail"/></svg>Cruises</div>
    <div><svg class="ic"><use href="#i-car"/></svg>Car Rentals</div>
    <div><svg class="ic"><use href="#i-people"/></svg>Package Tours</div>
    <div><svg class="ic"><use href="#i-plane"/></svg>Airfare</div>
  </div>
  <div class="ph p-people" role="img" aria-label="Happy couple with a map on a city street" style="left:218px;top:0;width:72px;height:105px"></div>
  <div class="brand" style="left:80px;top:8px">QELV</div>
  <div style="left:80px;top:28px;font-size:12px;font-weight:700;color:#333">QELV MAX</div>
  <div class="green" style="left:80px;top:48px;font-size:4.5px">Member's Only Website</div>
  <div class="tx" style="left:80px;top:60px;width:100px;color:#555">Over 500 National Brands<br>Save money while on vacation &amp; while at home</div>
  <ul class="dot-list" style="left:80px;top:116px;width:50px"><li>50 Year Membership $199 US / year Club Fee</li></ul>
  <ul class="dot-list" style="left:138px;top:116px;width:50px"><li>Expert Concierge Service</li></ul>
  <ul class="dot-list" style="left:208px;top:116px;width:50px"><li>2 Bonus Weeks</li></ul>
  <div class="tx" style="left:80px;top:136px;width:50px;font-style:italic">Book your stay today, enjoy it for life</div>
  <div class="tx" style="left:208px;top:136px;width:50px;font-style:italic">Plan your trip today and relax</div>
</section>

<!-- Row 3 -->
<section class="slide c1 r3">
  <div class="title" style="left:22px;top:30px">QELV <b>MAX</b></div>
  <svg class="ic yellow" style="left:24px;top:62px"><use href="#i-plane"/></svg>
  <div style="left:46px;top:60px;width:90px"><div class="lbl" style="text-transform:none">Flight Schedule</div><div class="tx">Book your flight, hotel, excursions and more all in one place.</div></div>
  <svg class="ic green" style="left:24px;top:90px"><use href="#i-bed"/></svg>
  <div style="left:46px;top:88px;width:90px"><div class="lbl" style="text-transform:none">Selected location</div><div class="tx">Book your flight, hotel, excursions and more all in one place.</div></div>
  <svg class="ic blue" style="left:24px;top:118px"><use href="#i-globe"/></svg>
  <div style="left:46px;top:116px;width:90px"><div class="lbl" style="text-transform:none">World wide</div><div class="tx">Book your flight, hotel, excursions and more all in one place.</div></div>
  <div class="ph p-pool" role="img" aria-label="Resort pool with sun umbrellas and palm trees" style="left:160px;top:0;width:130px;height:162px"></div>
  <div class="brand" style="left:4px;bottom:4px">QELV</div>
</section>

<section class="slide c2 r3">
  <div class="cap" style="left:19px;top:14px">Package based on adventure type</div>
  <div class="title" style="left:19px;top:24px">QELV MAX<br><b>Benefits</b></div>
  <div style="left:19px;top:60px;width:110px"><div class="lbl blue">Better Accommodations</div><div class="tx">Stay in suites around the world.</div></div>
  <div style="left:143px;top:60px;width:110px"><div class="lbl blue">Superior Service</div><div class="tx">Via telephone or internet.</div></div>
  <div style="left:19px;top:84px;width:100px"><div class="lbl blue">Flexibility</div><div class="tx">Book anything. Daily, weekly, no blackout dates, use as often as you wish and in as many rooms as you need.</div></div>
  <div style="left:143px;top:84px;width:100px"><div class="lbl blue">Substantial Savings</div><div class="tx">All types of travel. Share with Family and Friends.</div></div>
  <div class="strip" role="img" aria-label="Row of travel photos: coast, couple, city and hiker" style="left:0;top:124px;width:290px;height:38px">
    <span class="p-sea"></span><span class="p-room"></span><span class="p-beach"></span><span class="p-city"></span><span class="p-land"></span>
  </div>
</section>

<section class="slide c3 r3">
  <div class="title" style="left:30px;top:46px">QELV <b>MAX</b></div>
  <div class="tx" style="left:30px;top:64px;width:96px">Trip planning today can be challenging. With hundreds of websites, discount sites, hotels and accommodations it can seem overwhelming.</div>
  <div style="left:136px;top:42px;display:grid;grid-template-columns:repeat(3,42px);gap:4px" aria-label="Partner airlines">
    <div class="partner"><i style="background:#d8232a"></i></div>
    <div class="partner"><i style="background:#1e3a7a"></i></div>
    <div class="partner"><i style="background:#0b3c6b"></i></div>
    <div class="partner"><i style="background:#c8102e"></i></div>
    <div class="partner"><i style="background:#2a3e8f"></i></div>
    <div class="partner"><i style="background:#8a1c2b"></i></div>
    <div class="partner"><i style="background:#304cb2"></i></div>
    <div class="partner"><i style="background:#1b2f6b"></i></div>
    <div class="partner"><i style="background:#cc1f3d"></i></div>
  </div>
  <div class="brand" style="right:6px;bottom:4px">QELV</div>
</section>

<section class="slide c4 r3">
  <div class="title center" style="left:0;top:16px;width:290px">Check our rate &amp; packages</div>
  <div class="rate-card" style="left:26px;top:46px"><svg class="ic"><use href="#i-plane"/></svg><div class="name">Premier</div><div class="price bg-green">$1920</div><ul><li>Best services</li><li>Trusted since 1990</li><li>Low prices</li><li>Free booking fee</li></ul></div>
  <div class="rate-card" style="left:106px;top:46px"><svg class="ic"><use href="#i-globe"/></svg><div class="name">Power Exchange</div><div class="price bg-yellow"><s style="opacity:.7">$2666</s> $2199</div><ul><li>Best services</li><li>Trusted since 1990</li><li>Low prices</li><li>Free booking fee</li></ul></div>
  <div class="rate-card" style="left:186px;top:46px"><svg class="ic"><use href="#i-sun"/></svg><div class="name">Value Resorts</div><div class="price bg-blue">$8728</div><ul><li>Best services</li><li>Trusted since 1990</li><li>Low prices</li><li>Free booking fee</li></ul></div>
  <div class="brand" style="right:6px;bottom:3px">QELV</div>
</section>

<!-- Row 4 -->
<section class="slide c1 r4">
  <div class="ph p-hut" role="img" aria-label="Overwater bungalows on a turquoise lagoon" style="inset:0"></div>
  <div class="yellow center" style="left:0;top:20px;width:290px;font-size:4px">QELV MAX</div>
  <div class="white center" style="left:0;top:30px;width:290px;font-size:10px;font-weight:300;line-height:1.2">Exclusive Travel<br>Rewards For You</div>
  <div class="trip-card" style="left:56px;top:82px"><svg class="ic"><use href="#i-car"/></svg><div class="days">14 days Trip!</div><div class="bar bg-yellow">only $2827</div><div class="tx">Bali, Sulawesi, Papua</div></div>
  <div class="trip-card" style="left:124px;top:82px"><svg class="ic"><use href="#i-plane"/></svg><div class="days">14 days Trip!</div><div class="bar bg-green">only $2827</div><div class="tx">Bali, Sulawesi, Papua</div></div>
  <div class="trip-card" style="left:192px;top:82px"><svg class="ic"><use href="#i-sail"/></svg><div class="days">14 days Trip!</div><div class="bar bg-blue">only $2827</div><div class="tx">Bali, Sulawesi, Papua</div></div>
</section>

<section class="slide c2 r4">
  <div class="title center" style="left:0;top:12px;width:290px;font-weight:400">Begin Your Adventure</div>
  <div class="ph p-sea" role="img" aria-label="Tropical beach with huts" style="left:10px;top:31px;width:134px;height:62px"></div>
  <div class="ph p-pool" role="img" aria-label="Pier over a clear lagoon" style="left:144px;top:31px;width:134px;height:62px"></div>
  <div class="ph p-sun" role="img" aria-label="Deck chair on a sunny shore" style="left:10px;top:93px;width:134px;height:62px"></div>
  <div class="ph p-sea" role="img" aria-label="Calm blue sea and sky" style="left:144px;top:93px;width:134px;height:62px"></div>
  <div class="tile-label" style="left:10px;top:54px">Java<small>Indonesia</small></div>
  <div class="tile-label" style="left:144px;top:54px">Sumatra<small>Indonesia</small></div>
  <div class="tile-label" style="left:10px;top:116px">Seribu<small>Indonesia</small></div>
  <div class="tile-label" style="left:144px;top:116px">Borneo<small>Indonesia</small></div>
</section>

<section class="slide c3 r4">
  <div class="title center" style="left:0;top:24px;width:290px">Why Would I Own?</div>
  <div class="bg-blue" style="left:132px;top:44px;width:26px;height:2px"></div>
  <div class="own-card" style="left:8px;top:62px"><div class="lbl">Stay</div><div class="round p-people" role="img" aria-label="Couple on vacation"></div><div class="box">$12.99/night</div></div>
  <ul class="own-list" style="left:74px;top:64px;width:66px"><li>50 year membership</li><li>Pride of ownership</li><li>Exchange for new places</li><li>Improve your vacation lifestyle</li><li>Establish children's lifestyles</li><li>Privacy</li></ul>
  <div class="own-card" style="left:150px;top:62px"><div class="lbl">Friends</div><div class="round p-people" role="img" aria-label="Friends laughing together"></div><div class="box">$12.99/night</div></div>
  <ul class="own-list" style="left:216px;top:64px;width:66px"><li>Freeze ownership costs of future vacations</li><li>Luxury, fully furnished accommodations</li><li>Ownership with deed and title</li><li>Price guarantee</li><li>Loan your week to a friend or relative</li><li>Guaranteed opt out</li></ul>
  <div class="brand" style="right:6px;bottom:3px">QELV</div>
</section>

<section class="slide c4 r4">
  <div class="title center" style="left:0;top:20px;width:290px">QELV <b>MAX</b></div>
  <div class="tx center" style="left:30px;top:56px;width:230px">Trip planning today can be challenging. With hundreds of websites, discount sites, hotels and accommodations it can seem overwhelming. QELV MAX is the exclusive service, offering premium travel opportunities at discount rates. Book your flight, hotel, excursions and more all in one place.</div>
  <div class="feat" style="left:20px;top:86px;width:250px;grid-template-columns:repeat(3,1fr)">
    <div><svg class="ic yellow" style="margin:0 auto 4px"><use href="#i-plane"/></svg><div class="lbl">Stay</div><div class="tx">Rent or bid on weekly stay vacations. Make an offer for a price you want to pay</div></div>
    <div><svg class="ic green" style="margin:0 auto 4px"><use href="#i-sail"/></svg><div class="lbl">Logistics</div><div class="tx">Rent or bid on weekly stay vacations. Make an offer for a price you want to pay</div></div>
    <div><svg class="ic blue" style="margin:0 auto 4px"><use href="#i-sail"/></svg><div class="lbl">Sail &amp; Fishing</div><div class="tx">Rent or bid on weekly stay vacations. Make an offer for a price you want to pay</div></div>
  </div>
  <div class="brand" style="right:6px;bottom:3px">QELV</div>
</section>

<!-- Row 5 -->
<section class="slide c1 r5">
  <div class="title center" style="left:0;top:14px;width:290px">QELV <b>MAX</b></div>
  <div class="feat" style="left:20px;top:42px;width:250px;grid-template-columns:repeat(3,1fr);row-gap:6px">
    <div><svg class="ic green" style="margin:0 auto 3px"><use href="#i-plane"/></svg><div class="lbl">Reward Credits</div><div class="tx">Rent or bid on weekly stay vacations. Make an offer for a price you want to pay</div></div>
    <div><svg class="ic green" style="margin:0 auto 3px"><use href="#i-sail"/></svg><div class="lbl">400,000+ Hotels</div><div class="tx">Rent or bid on weekly stay vacations. Make an offer for a price you want to pay</div></div>
    <div><svg class="ic green" style="margin:0 auto 3px"><use href="#i-tag"/></svg><div class="lbl">Marketplace</div><div class="tx">Rent or bid on weekly stay vacations. Make an offer for a price you want to pay</div></div>
    <div><svg class="ic yellow" style="margin:0 auto 3px"><use href="#i-sun"/></svg><div class="lbl">Orbit</div><div class="tx">Rent or bid on weekly stay vacations. Make an offer for a price you want to pay</div></div>
    <div><svg class="ic yellow" style="margin:0 auto 3px"><use href="#i-sail"/></svg><div class="lbl">Price Guarantee</div><div class="tx">Rent or bid on weekly stay vacations. Make an offer for a price you want to pay</div></div>
    <div><svg class="ic yellow" style="margin:0 auto 3px"><use href="#i-people"/></svg><div class="lbl">Live Chat</div><div class="tx">Rent or bid on weekly stay vacations. Make an offer for a price you want to pay</div></div>
  </div>
  <div class="brand" style="right:6px;bottom:3px">QELV</div>
</section>

<section class="slide c2 r5">
  <div class="ph p-hut" role="img" aria-label="Beach resort with palm trees by the sea" style="left:120px;top:0;width:170px;height:96px"></div>
  <div class="cap" style="left:29px;top:12px;text-transform:none">QELV <b>MAX</b></div>
  <div class="title" style="left:29px;top:22px;font-weight:400">Exclusive Travel<br>Rewards For<br>You</div>
  <div class="yellow" style="left:38px;top:110px;font-size:7px;letter-spacing:2px">★★★★★</div>
  <div class="btn bg-green" style="left:29px;top:128px;width:62px;height:12px;text-transform:none">Scandinavia Trip</div>
  <div class="tx" style="left:107px;top:114px;width:170px">Trip planning today can be challenging. With hundreds of websites, discount sites, hotels and accommodations it can seem overwhelming. QELV MAX is the exclusive service, offering premium travel opportunities at discount rates. Book your flight, hotel, excursions and more all in one place.</div>
  <div class="brand" style="right:6px;bottom:3px">QELV</div>
</section>

<section class="slide c3 r5">
  <div class="ph p-sun" role="img" aria-label="Lounge chair beside an infinity pool at sunset" style="left:16px;top:16px;width:154px;height:134px"></div>
  <div class="dest-card" style="left:160px;top:30px">
    <div class="name">Thailand</div><div class="cap">+ Brunei / Indonesia</div>
    <div class="bar">10 Destinations in 3 Days</div>
    <div class="icons"><svg class="ic green"><use href="#i-hotel"/></svg><svg class="ic green"><use href="#i-plane"/></svg><svg class="ic green"><use href="#i-sun"/></svg></div>
    <div class="tx">QELV MAX is the exclusive service, offering premium travel opportunities at discount rates.</div>
  </div>
  <div class="brand" style="right:6px;bottom:3px">QELV</div>
</section>

<section class="slide c4 r5">
  <div class="ph p-pool" role="img" aria-label="Resort pool lined with sun loungers" style="left:116px;top:16px;width:150px;height:124px"></div>
  <div class="dest-card" style="left:32px;top:30px">
    <div class="name">Indonesia</div><div class="cap">+ Fiji / Papua NG</div>
    <div class="bar">10 Destinations in 3 Days</div>
    <div class="icons"><svg class="ic"><use href="#i-hotel"/></svg><svg class="ic"><use href="#i-plane"/></svg><svg class="ic"><use href="#i-sun"/></svg></div>
    <div class="tx">QELV MAX is the exclusive service, offering premium travel opportunities at discount rates.</div>
  </div>
  <div class="brand" style="left:4px;bottom:3px">QELV</div>
</section>

<!-- Row 6 -->
<section class="slide c1 r6">
  <div class="ph p-land" role="img" aria-label="Rolling countryside under a bright sky" style="left:0;top:0;width:290px;height:68px"></div>
  <div class="white" style="left:18px;top:12px;font-size:10px;font-weight:300">Discover</div>
  <div class="pack" style="left:40px;top:36px;width:70px;height:106px"><div class="img p-pool" role="img" aria-label="Pool villa"></div><div class="kind">COMPLETE PACK</div><div class="name">THAILAND</div><div class="tx">Book your flight, hotel, excursions and more.</div><div class="meta"><span>DAYS<b>3 days, 2 night</b></span><span>HOTELS<b>5 stars</b></span></div></div>
  <div class="pack" style="left:110px;top:28px;width:72px;height:120px"><div class="img p-room" role="img" aria-label="Hotel bedroom"></div><div class="kind">COMPLETE PACK</div><div class="name">BALI + LOMBOK</div><div class="tx">Book your flight, hotel, excursions and more.</div><div class="meta"><span>DAYS<b>3 days, 2 night</b></span><span>HOTELS<b>5 stars</b></span></div></div>
  <div class="pack" style="left:182px;top:36px;width:70px;height:106px"><div class="img p-sea" role="img" aria-label="Island boats on clear water"></div><div class="kind">COMPLETE PACK</div><div class="name">FIJI ISLANDS</div><div class="tx">Book your flight, hotel, excursions and more.</div><div class="meta"><span>DAYS<b>3 days, 2 night</b></span><span>HOTELS<b>5 stars</b></span></div></div>
  <div class="brand" style="left:4px;bottom:3px">QELV</div>
</section>

<section class="slide c2 r6">
  <div class="ph p-jungle" role="img" aria-label="Waterfall in a lush rainforest" style="left:0;top:0;width:290px;height:80px"></div>
  <div class="white" style="left:22px;top:32px;font-size:10px;font-weight:300;line-height:1.2">Exclusive Travel<br>Rewards For You</div>
  <div class="tx" style="left:22px;top:90px;width:146px;color:#777">Trip planning today can be challenging. With hundreds of websites, discount sites, hotels and accommodations it can seem overwhelming. QELV MAX is the exclusive service, offering premium travel opportunities at discount rates. Book your flight, hotel, excursions and more all in one place.</div>
  <div class="pack" style="left:176px;top:34px;width:90px;height:106px"><div class="img p-room" role="img" aria-label="Hotel bedroom" style="height:48px"></div><div class="kind">COMPLETE PACK</div><div class="name">BALI + LOMBOK</div><div class="tx">Book your flight, hotel, excursions and more.</div><div class="meta"><span>DAYS<b>3 days, 2 night</b></span><span>HOTELS<b>5 stars</b></span></div></div>
  <div class="brand" style="left:4px;bottom:3px">QELV</div>
</section>

<section class="slide c3 r6">
  <div class="ph p-room" role="img" aria-label="Bright hotel bedroom with large bed" style="left:17px;top:18px;width:124px;height:130px"></div>
  <div class="title" style="left:137px;top:18px;margin-left:0">Exclusive Travel<br>Rewards For You</div>
  <div class="bg-yellow btn" style="left:137px;top:54px;width:36px;height:24px;flex-direction:column;font-size:2.8px"><svg class="ic" style="fill:#fff"><use href="#i-plane"/></svg>BUDGET FLIGHT</div>
  <div style="left:180px;top:56px;display:flex;gap:14px" class="blue">
    <div class="cap center"><svg class="ic" style="margin:0 auto 2px;fill:var(--blue)"><use href="#i-people"/></svg>GROUP TRIP</div>
    <div class="cap center"><svg class="ic" style="margin:0 auto 2px;fill:var(--blue)"><use href="#i-hotel"/></svg>NEAR HOTELS</div>
  </div>
  <div class="tx" style="left:137px;top:90px;width:140px">Trip planning today can be challenging. With hundreds of websites, discount sites, hotels and accommodations it can seem overwhelming. QELV MAX is the exclusive service, offering premium travel opportunities at discount rates.</div>
  <div class="btn bg-green" style="left:137px;top:126px;width:88px;height:12px;font-size:3.4px">20% Discount During Summer</div>
  <div class="brand" style="right:6px;bottom:3px">QELV</div>
</section>

<section class="slide c4 r6">
  <div class="ph p-hut" role="img" aria-label="Overwater villas in a tropical lagoon" style="left:0;top:0;width:290px;height:82px"></div>
  <div class="white center" style="left:0;top:22px;width:290px;font-size:10px;font-weight:300;line-height:1.2">Budget Trip, Save More<br>Money in Group</div>
  <div class="bg-green btn" style="left:42px;top:68px;width:34px;height:30px;flex-direction:column;font-size:2.8px"><svg class="ic" style="fill:#fff"><use href="#i-plane"/></svg>BUDGET FLIGHT</div>
  <div style="left:76px;top:68px;width:172px;height:30px;background:#fff;display:flex;justify-content:space-around;align-items:center">
    <div class="cap center"><svg class="ic yellow" style="margin:0 auto 2px"><use href="#i-people"/></svg>GROUP TRIP</div>
    <div class="cap center"><svg class="ic blue" style="margin:0 auto 2px"><use href="#i-hotel"/></svg>NEAR HOTELS</div>
    <div class="cap center"><svg class="ic green" style="margin:0 auto 2px"><use href="#i-people"/></svg>PRO. GUIDE</div>
    <div class="cap center"><svg class="ic" style="margin:0 auto 2px;fill:#666"><use href="#i-sail"/></svg>SAIL &amp; FISHING</div>
  </div>
  <div class="tx center" style="left:24px;top:104px;width:242px">Trip planning today can be challenging. With hundreds of websites, discount sites, hotels and accommodations it can seem overwhelming. QELV MAX is the exclusive service, offering premium travel opportunities at discount rates. Book your flight, hotel, excursions and more all in one place.</div>
  <div class="brand" style="right:6px;bottom:3px">QELV</div>
</section>

<!-- Row 7 -->
<section class="slide c1 r7 grey">
  <div class="title center" style="left:0;top:12px;width:290px;font-weight:400">Event Calendar</div>
  <div style="left:30px;top:40px;width:70px;height:112px;background:#f3f3f3;padding:8px 10px">
    <div class="cap" style="font-weight:700;color:#333">▣ December 2020</div>
    <div style="font-size:7px;margin:8px 0 5px;line-height:1.15">Mountain<br>Survival</div>
    <div class="tx">QELV MAX is the exclusive service, offering premium travel opportunities at discount rates.</div>
  </div>
  <div class="event" style="left:100px;top:30px;width:88px;height:128px;box-shadow:0 1px 3px rgba(0,0,0,.2)"><div class="img p-pool" role="img" aria-label="Resort pool at dusk"></div><div class="free">BOOKING FREE</div><div class="date">▣ SEPTEMBER 2019</div><div class="name">Wild West Wave</div><div class="tx">QELV MAX is the exclusive service, offering premium travel opportunities at discount rates.</div></div>
  <div style="left:188px;top:40px;width:72px;height:112px;background:#dff1d2;padding:8px 10px">
    <div class="cap" style="font-weight:700;color:#333">▣ October 2019</div>
    <div style="font-size:7px;margin:8px 0 5px;line-height:1.15">Backpacker<br>Badgers</div>
    <div class="tx">QELV MAX is the exclusive service, offering premium travel opportunities at discount rates.</div>
    <div class="meta tx" style="margin-top:6px;display:flex;justify-content:space-between"><span>DAYS<br><b class="yellow" style="font-weight:400">3 days, 2 night</b></span><span>HOTELS<br><b class="yellow" style="font-weight:400">5 stars</b></span></div>
  </div>
  <div class="brand" style="left:4px;bottom:3px">QELV</div>
</section>

<section class="slide c2 r7 grey">
  <div class="title center" style="left:0;top:12px;width:290px;font-weight:400">Event Calendar</div>
  <div class="event" style="left:12px;top:30px;width:86px;height:128px"><div class="img p-people" role="img" aria-label="Travelers with a map"></div><div class="free">BOOKING FREE</div><div class="date">▣ SEPTEMBER 2019</div><div class="name">Wild West Wave</div><div class="tx">QELV MAX is the exclusive service, offering premium travel opportunities at discount rates.</div></div>
  <div class="event" style="left:102px;top:30px;width:86px;height:128px"><div class="img p-jungle" role="img" aria-label="Misty mountain forest"></div><div class="free">BOOKING FREE</div><div class="date">▣ SEPTEMBER 2019</div><div class="name">Top Peak</div><div class="tx">QELV MAX is the exclusive service, offering premium travel opportunities at discount rates.</div></div>
  <div class="event" style="left:192px;top:30px;width:86px;height:128px"><div class="img p-land" role="img" aria-label="Hiker on a grassy ridge"></div><div class="free">BOOKING FREE</div><div class="date">▣ SEPTEMBER 2019</div><div class="name">Cliff Camp</div><div class="tx">QELV MAX is the exclusive service, offering premium travel opportunities at discount rates.</div></div>
</section>

<section class="slide c3 r7 grey">
  <div class="title center" style="left:0;top:12px;width:290px;font-weight:400">Choose Your Best</div>
  <div class="offer" style="left:16px;top:30px"><div class="img p-city" role="img" aria-label="White seaside village"></div><div class="info"><div class="price">$35 <small>FOR PERSON PER NIGHT</small></div><div class="tx">Book your flight, hotel, excursions and more all in one place.</div><div class="dots"><i></i><i></i><i></i></div></div></div>
  <div class="offer" style="left:148px;top:30px"><div class="img p-city" role="img" aria-label="City hotel tower"></div><div class="info"><div class="price">$35 <small>FOR PERSON PER NIGHT</small></div><div class="tx">Book your flight, hotel, excursions and more all in one place.</div><div class="dots"><i></i><i></i><i></i></div></div></div>
  <div class="offer" style="left:16px;top:92px"><div class="img p-room" role="img" aria-label="Boutique hotel entrance"></div><div class="info"><div class="price">$35 <small>FOR PERSON PER NIGHT</small></div><div class="tx">Book your flight, hotel, excursions and more all in one place.</div><div class="dots"><i></i><i></i><i></i></div></div></div>
  <div class="offer" style="left:148px;top:92px"><div class="img p-pool" role="img" aria-label="Resort pool with palms"></div><div class="info"><div class="price">$35 <small>FOR PERSON PER NIGHT</small></div><div class="tx">Book your flight, hotel, excursions and more all in one place.</div><div class="dots"><i></i><i></i><i></i></div></div></div>
</section>

<section class="slide c4 r7">
  <div class="side">
    <div><svg class="ic"><use href="#i-tag"/></svg>Free Delicious<br>Breakfast</div>
    <div><svg class="ic"><use href="#i-bed"/></svg>Free 1 Extra<br>Bed</div>
    <div><svg class="ic"><use href="#i-star"/></svg>Pet Friendly</div>
    <div><svg class="ic"><use href="#i-people"/></svg>Family Game<br>and Play</div>
  </div>
  <div class="ph p-city" role="img" aria-label="Couple reading a map in front of a grand old building" style="left:68px;top:0;width:222px;height:162px"></div>
</section>

</body>
</html>
```